Label for kTw Ranch beef tallow

I need a small label to go on a 2oz amber glass jar as well as a 4 oz. amber glass jar of moisturizer.
I prefer it to be rectangular for the 2oz jar since it's small and square for the 4oz jar.
I'd like to keep our kTw Ranch logo the same font and style, which is attached. Ten Sleep, Wyoming should be left out. The font for kTw Ranch is spartan.
The label content is as follows:
Meadowlark Balm
Whipped Moisturizer
Ingredients: Beef Tallow, jojoba oil, peppermint oil.
2oz. jar

Instead of a white label, I'm thinking of a tan or brown label that will blend in with the amber jar. The lettering could then be a white, cream or even rust/burgandy color. Something to give it a rich look.

Thank you!

Target Market(s)

Mainly women but men as well.

Industry/Entity Type

Ranching and online beef sales

Requirements
Must have
• kTw Ranch logo

```html
<!DOCTYPE html>
<html lang="en">
<head>
<meta charset="utf-8">
<title>kTw Ranch Whipped Moisturizer Labels</title>
<link rel="stylesheet" href="https://fonts.googleapis.com/css2?family=League+Spartan:wght@400;600&display=swap">
<style>
  :root {
    --backdrop: #e6e6e6;
    --label-paper: #ffffff;
    --ink: #000000;
    --band-text: #ffffff;
  }
  * { margin: 0; padding: 0; box-sizing: border-box; }
  html, body { width: 1200px; height: 1200px; overflow: hidden; }
  body {
    background: var(--backdrop);
    font-family: "League Spartan", sans-serif;
    color: var(--ink);
    position: relative;
  }
  .label {
    position: absolute;
    background: var(--label-paper);
    border-radius: 32px;
    overflow: hidden;
  }
  .label-small { left: 40px; top: 440px; width: 542px; height: 322px; }
  .label-large { left: 640px; top: 330px; width: 522px; height: 522px; }

  .band {
    position: absolute;
    background: var(--ink);
    color: var(--band-text);
    display: flex;
    align-items: center;
    justify-content: center;
    white-space: nowrap;
    letter-spacing: 0.02em;
    font-weight: 400;
  }
  .label-small .band {
    left: 91px; top: 32px; width: 39px; height: 290px;
    font-size: 24px;
  }
  .label-small .band span { transform: rotate(-90deg); display: block; padding-top: 4px; }
  .label-large .band {
    left: 0; top: 65px; width: 100%; height: 45px;
    font-size: 38px; padding-top: 6px;
  }

  .content {
    position: absolute;
    text-align: center;
    display: flex;
    flex-direction: column;
    align-items: center;
  }
  .label-small .content { left: 130px; right: 0; top: 0; bottom: 0; }
  .label-large .content { left: 0; right: 0; top: 0; bottom: 0; }

  .brand-name { font-weight: 400; line-height: 1; white-space: nowrap; }
  .product-name { font-weight: 600; line-height: 1; letter-spacing: 0.01em; }
  .ingredients { font-weight: 600; line-height: 1; }
  .size { font-weight: 600; line-height: 1; }

  .label-small .brand-name { font-size: 56px; margin-top: 112px; }
  .label-small .product-name { font-size: 25px; margin-top: 52px; }
  .label-small .ingredients { font-size: 13px; margin-top: 10px; }
  .label-small .size { font-size: 13px; margin-top: 16px; }

  .label-large .brand-name { font-size: 74px; margin-top: 212px; }
  .label-large .product-name { font-size: 35px; margin-top: 90px; }
  .label-large .ingredients { font-size: 20px; margin-top: 14px; }
  .label-large .size { font-size: 16px; margin-top: 26px; }
</style>
</head>
<body>
  <section class="label label-small" aria-label="2 oz jar label">
    <div class="band"><span>MEADOWLARK BALM</span></div>
    <div class="content">
      <p class="brand-name">kTw Ranch</p>
      <p class="product-name">WHIPPED MOISTURIZER</p>
      <p class="ingredients">Beef Tallow, jojoba oil, peppermint oil</p>
      <p class="size">2oz.</p>
    </div>
  </section>

  <section class="label label-large" aria-label="4 oz jar label">
    <div class="band">MEADOWLARK BALM</div>
    <div class="content">
      <p class="brand-name">kTw Ranch</p>
      <p class="product-name">WHIPPED MOISTURIZER</p>
      <p class="ingredients">Beef Tallow, jojoba oil, peppermint oil</p>
      <p class="size">4oz.</p>
    </div>
  </section>
</body>
</html>
```